Quillbrook Nourish

We are a nutritional coaching business who specalise in:

Weight Loss
Improved Body Composition
Personalised Meal Plans
Health & Vitality

We are in the process of developing a facebook page and need a cover photo design. Our logo has already been created which we will use for the profile pic. We would like the background to be simple and include our logo as well as the 4 dot points above.

Project Deadline Extended Reason: Going to commit the funds nows everyone, however would just like to extend the time frame only for a short period to get more designs. Added Friday, January 09, 2015

• Please make sure the design will upload easily to facebook, specifically the cover photo and not become distorted.

```html
<!DOCTYPE html>
<html lang="en">
<head>
<meta charset="utf-8">
<title>Quillbrook Nourish – Cover</title>
<link rel="stylesheet" href="https://fonts.googleapis.com/css2?family=Cabin:wght@600;700&family=Open+Sans:wght@400&family=Arimo:wght@400;700&display=swap">
<style>
  :root {
    --lime-light: #d6ea9a;
    --lime-mid: #a9d162;
    --lime-deep: #7db53a;
    --orange: #f5a33a;
    --green: #1f8a3e;
    --blue: #3d67a8;
    --red: #b41f2a;
    --white: #ffffff;
    --ink: #1b1b1b;
    --brand-blue: #2f7fc1;
    --button-bg: #f6f7f9;
    --button-border: #cfd2d8;
    --button-text: #4b4f56;
  }
  html, body {
    margin: 0;
    padding: 0;
    width: 1200px;
    height: 456px;
    overflow: hidden;
    background: var(--white);
  }
  .cover {
    position: relative;
    width: 1200px;
    height: 456px;
    overflow: hidden;
    background:
      radial-gradient(circle at 62% 45%, rgba(255,255,255,0.55) 0, rgba(255,255,255,0) 38%),
      radial-gradient(circle at 20% 30%, rgba(255,255,255,0.25) 0, rgba(255,255,255,0) 30%),
      linear-gradient(90deg, var(--lime-deep) 0%, var(--lime-mid) 35%, var(--lime-light) 60%, var(--lime-mid) 100%);
  }
  .apple-silhouette {
    position: absolute;
    left: 585px;
    top: 30px;
    width: 330px;
    height: 420px;
    border-radius: 48% 48% 46% 46%;
    background: radial-gradient(ellipse at 50% 50%, rgba(140,190,80,0.35), rgba(140,190,80,0) 70%);
  }
  .lime-illustration {
    position: absolute;
    left: 900px;
    top: -4px;
    width: 298px;
    height: 244px;
    background:
      radial-gradient(ellipse 108px 122px at 108px 118px, #f3f5b0 0, #dbe67a 55%, #8cc23c 78%, #3f8f2a 96%, rgba(63,143,42,0) 100%),
      radial-gradient(ellipse 60px 70px at 240px 160px, rgba(80,150,60,0.85) 0, rgba(80,150,60,0) 100%);
  }
  .service-icon {
    position: absolute;
    width: 84px;
    height: 84px;
    filter: drop-shadow(4px 4px 0 rgba(0,0,0,0.85));
  }
  .service-label {
    position: absolute;
    margin: 0;
    font-family: "Cabin", sans-serif;
    font-weight: 700;
    line-height: 1;
    color: var(--white);
    text-shadow: 3px 3px 0 var(--ink);
    white-space: nowrap;
  }
  .service-label .accent {
    text-shadow: 0 0 2px var(--white), 0 0 2px var(--white), 2px 2px 0 rgba(255,255,255,0.9);
  }
  .accent.orange { color: var(--orange); }
  .accent.green { color: var(--green); }
  .accent.blue { color: var(--blue); }
  .accent.red { color: var(--red); }

  .icon-weight { left: 30px; top: 22px; }
  .icon-eating { left: 460px; top: 20px; }
  .icon-body { left: 28px; top: 134px; }
  .icon-vitality { left: 460px; top: 142px; }

  .label-weight { left: 146px; top: 40px; font-size: 54px; }
  .label-eating { left: 560px; top: 46px; font-size: 44px; }
  .label-body { left: 146px; top: 138px; font-size: 42px; line-height: 44px; text-align: center; }
  .label-vitality { left: 560px; top: 164px; font-size: 44px; }

  .profile-frame {
    position: absolute;
    left: 24px;
    top: 243px;
    width: 230px;
    height: 213px;
    background: var(--white);
    border: 1px solid #d3d6db;
    box-sizing: border-box;
    display: flex;
    align-items: center;
    justify-content: center;
  }
  .profile-name {
    font-family: "Cabin", sans-serif;
    font-weight: 600;
    font-size: 21px;
    color: var(--brand-blue);
    text-align: center;
  }
  .page-title {
    position: absolute;
    left: 283px;
    top: 334px;
    margin: 0;
    font-family: "Open Sans", sans-serif;
    font-weight: 400;
    font-size: 35px;
    line-height: 42px;
    color: var(--white);
  }
  .page-button {
    position: absolute;
    box-sizing: border-box;
    background: var(--button-bg);
    border: 1px solid var(--button-border);
    border-radius: 2px;
    font-family: "Arimo", sans-serif;
    font-weight: 700;
    font-size: 14px;
    color: var(--button-text);
    display: flex;
    align-items: center;
    justify-content: center;
  }
  .button-update { left: 970px; top: 322px; width: 209px; height: 40px; }
  .button-log { left: 902px; top: 384px; width: 224px; height: 33px; }
  .button-more { left: 1129px; top: 384px; width: 50px; height: 33px; font-size: 18px; letter-spacing: 1px; }
</style>
</head>
<body>
<main class="cover">
  <div class="apple-silhouette" role="img" aria-label="Faint apple and leaf silhouette in the background"></div>
  <div class="lime-illustration" role="img" aria-label="Illustration of a halved lime with water droplets and leaves"></div>

  <svg class="service-icon icon-weight" viewBox="0 0 88 88" aria-hidden="true">
    <circle cx="44" cy="44" r="42" fill="var(--orange)"/>
    <rect x="24" y="22" width="40" height="46" rx="10" fill="none" stroke="#fff" stroke-width="4"/>
    <circle cx="44" cy="40" r="11" fill="none" stroke="#fff" stroke-width="3.5"/>
    <line x1="44" y1="40" x2="50" y2="33" stroke="#fff" stroke-width="3" stroke-linecap="round"/>
  </svg>
  <p class="service-label label-weight"><span class="accent orange">Weight</span> Loss</p>

  <svg class="service-icon icon-eating" viewBox="0 0 88 88" aria-hidden="true">
    <circle cx="44" cy="44" r="42" fill="var(--green)"/>
    <path d="M26 24 L62 62" stroke="#fff" stroke-width="7" stroke-linecap="round"/>
    <path d="M60 22 L54 32 L40 48 L28 62" stroke="#fff" stroke-width="5" stroke-linecap="round" fill="none"/>
    <path d="M54 20 L52 34 M66 30 L56 36 M62 24 L54 34" stroke="#fff" stroke-width="3" stroke-linecap="round"/>
  </svg>
  <p class="service-label label-eating"><span class="accent green">Healthy</span> Eating</p>

  <svg class="service-icon icon-body" viewBox="0 0 88 88" aria-hidden="true">
    <circle cx="44" cy="44" r="42" fill="var(--blue)"/>
    <g transform="rotate(-45 44 44)" fill="#fff">
      <rect x="22" y="40" width="44" height="8" rx="2"/>
      <rect x="18" y="30" width="8" height="28" rx="2"/>
      <rect x="28" y="33" width="6" height="22" rx="2"/>
      <rect x="62" y="30" width="8" height="28" rx="2"/>
      <rect x="54" y="33" width="6" height="22" rx="2"/>
    </g>
  </svg>
  <p class="service-label label-body"><span class="accent blue">Improved Body</span><br>Composition</p>

  <svg class="service-icon icon-vitality" viewBox="0 0 88 88" aria-hidden="true">
    <circle cx="44" cy="44" r="42" fill="var(--red)"/>
    <path d="M44 68 C20 50 16 38 22 29 C28 20 40 22 44 32 C48 22 60 20 66 29 C72 38 68 50 44 68 Z" fill="#fff"/>
    <path d="M20 46 H34 L38 38 L43 54 L48 32 L53 50 L56 44 H68" stroke="var(--red)" stroke-width="3" fill="none" stroke-linejoin="round"/>
  </svg>
  <p class="service-label label-vitality"><span class="accent red">Health and</span> Vitality</p>

  <div class="profile-frame">
    <span class="profile-name">Quillbrook Nourish</span>
  </div>

  <h1 class="page-title">QUILLBROOK<br>NOURISH</h1>

  <div class="page-button button-update">Actualizar información</div>
  <div class="page-button button-log">Ver registro de actividad</div>
  <div class="page-button button-more">•••</div>
</main>
</body>
</html>
```